Flyer Design Project

We are a restaurant delivery service. We deliver from a variety of restaurants. We are looking for a small flyer that we will put on the front desk at a restaurant that says "We Deliver!" Include our website trovaloopcourier.com and phone number 833-9 Gem Lamp! We would like the emphasis to be on ordering online. The flyer size should be 4.25" x 5.5".

```html
<!DOCTYPE html>
<html lang="en">
<head>
<meta charset="UTF-8">
<title>Trovaloop Courier – We Deliver! Flyer</title>
<link rel="stylesheet" href="https://fonts.googleapis.com/css2?family=Open+Sans:wght@600&family=Titan+One&family=Ubuntu:wght@700&family=Saira:ital,wght@1,700&family=Archivo+Black&display=swap">
<style>
  :root {
    --flyer-red: #e20613;
    --paper-white: #ffffff;
    --cream-outline: #fbf3a0;
    --ink-black: #111111;
    --url-yellow: #ffee00;
  }
  html, body {
    margin: 0;
    width: 1200px;
    height: 1000px;
    overflow: hidden;
    background: var(--paper-white);
  }
  .flyer {
    position: absolute;
    left: 0;
    top: 0;
    width: 1200px;
    height: 1000px;
    display: block;
  }
  .brand-name {
    font-family: "Open Sans", sans-serif;
    font-weight: 600;
    fill: var(--paper-white);
  }
  .phone-number {
    font-family: "Titan One", sans-serif;
    font-size: 118px;
  }
  .phone-number-shadow { fill: var(--ink-black); }
  .phone-number-main {
    fill: var(--flyer-red);
    stroke: var(--cream-outline);
    stroke-width: 9px;
    paint-order: stroke;
    stroke-linejoin: round;
  }
  .headline {
    font-family: "Ubuntu", sans-serif;
    font-weight: 700;
    font-size: 70px;
    fill: var(--paper-white);
  }
  .tagline {
    font-family: "Saira", sans-serif;
    font-style: italic;
    font-weight: 700;
    font-size: 76px;
    fill: var(--paper-white);
  }
  .website {
    font-family: "Archivo Black", sans-serif;
    font-size: 40px;
    stroke-linejoin: round;
  }
  .website-halo {
    fill: var(--flyer-red);
    stroke: var(--flyer-red);
    stroke-width: 14px;
  }
  .website-main {
    fill: var(--url-yellow);
    stroke: var(--ink-black);
    stroke-width: 3px;
    paint-order: stroke;
  }
</style>
</head>
<body>
<svg class="flyer" viewBox="0 0 1200 1000" xmlns="http://www.w3.org/2000/svg">
  <rect class="card-background" x="400" y="178" width="421" height="545" fill="var(--flyer-red)"/>
  <path class="online-band" d="M400 656 Q610 585 821 656 L821 713 L400 713 Z" fill="var(--paper-white)"/>

  <text class="brand-name" x="610" y="262" font-size="44" text-anchor="middle">Trovaloop Courier</text>

  <g class="phone-number" text-anchor="middle">
    <text class="phone-number-shadow" x="617" y="420" textLength="366" lengthAdjust="spacingAndGlyphs">833-9</text>
    <text class="phone-number-main" x="613" y="414" textLength="366" lengthAdjust="spacingAndGlyphs">833-9</text>
  </g>

  <text class="headline" x="613" y="501" text-anchor="middle" textLength="382" lengthAdjust="spacingAndGlyphs">We Deliver!</text>
  <text class="tagline" x="614" y="592" text-anchor="middle" textLength="384" lengthAdjust="spacingAndGlyphs">Gem Lamp!</text>

  <g class="website" text-anchor="middle">
    <text class="website-halo" x="609" y="695" textLength="396" lengthAdjust="spacingAndGlyphs">trovaloopcourier.com</text>
    <text class="website-main" x="609" y="695" textLength="396" lengthAdjust="spacingAndGlyphs">trovaloopcourier.com</text>
  </g>
</svg>
</body>
</html>
```